Norvale Works - pioneers of next generation consulting!

We are a next generation management consulting firm with two focus areas and USPs (unique selling points):>Technology driven business developmentWe are not developers, we are experts in HOW to apply and incorporate technology in your business dna to drive business growth and value-added change.>Creating high performing teams levering our philosophy of collective intelligence. We truly understand the need of human engagement and we know that the only way of getting there is by building strong relationships among people, a warm and open culture is a stepping stone towards effective collaboration within/among teams. - We don't want a ”corporate feel” to our templates. The organic feeling we have with our blue-on-blue blobs has the idea of ever changing movement and shape changing. Please see our website, www.norvaleworks.se. - In our context we sit among classic business mgmt. consultants and classic IT mgmt. consultants. We cater to business, tech and humans as the ultimate vehicle of change and business value. -To have a clean template one suggestion is to only use blue, white and black and keeping other colors separate, as an alternative but we are truly open allow your creativity add value to this. We are looking to find a slide deck which we can pick slides from, depending on what/whom/why we interact with customer we want to create different outcomes and our presentations should support this.

Industry/Entity Type

Management Consulting

Requirements
Must have
• next generation powerpoint and how to package storytelling. please keep to our look and feel, we just arrived at our logo, colours and shapes. Help us to carry it into our ppt's as well.
Should not have
• Hi all, please have a look at our website. It is still very new and more will be done, but our goal is to make powerpoint to come alive again and mirror our pioneering hearts and brains.

```html
<!DOCTYPE html>
<html lang="en">
<head>
<meta charset="utf-8">
<title>Norvale Works – Slide Deck Template</title>
<link href="https://fonts.googleapis.com/css2?family=Lato:wght@300;400;700&display=swap" rel="stylesheet">
<style>
  :root {
    --page: #f1f1f3;
    --white: #ffffff;
    --blue: #2b62cc;
    --blue-deep: #1c4aa8;
    --navy: #173a80;
    --glow: #6f9ff0;
    --shade: #14378a;
    --ink: #1d3263;
    --body: #3b404c;
    --mist: #e2e8f3;
    --photo-warm-a: #5d4b3c;
    --photo-warm-b: #c9b8a2;
    --photo-grey-a: #8b8f96;
    --photo-grey-b: #dcdde0;
  }
  * { margin: 0; padding: 0; box-sizing: border-box; }
  html, body { width: 857px; height: 1200px; overflow: hidden; background: var(--page); }
  body { font-family: "Lato", Arial, sans-serif; }

  .canvas { width: 857px; height: 1200px; overflow: hidden; position: relative; }
  .deck { width: 1000px; height: 1400px; position: relative; transform: scale(0.857); transform-origin: 0 0; }

  .slide { position: absolute; width: 480px; height: 270px; overflow: hidden; background: var(--white); }
  .col-a { left: 10px; } .col-b { left: 510px; }
  .row-1 { top: 5px; } .row-2 { top: 285px; } .row-3 { top: 565px; } .row-4 { top: 845px; } .row-5 { top: 1125px; }

  .slide svg.deco { position: absolute; inset: 0; width: 480px; height: 270px; }
  .photo { position: absolute; }

  .brand { position: absolute; font-weight: 700; letter-spacing: 0.5px; text-transform: uppercase; white-space: nowrap; }
  .brand-light { color: var(--white); }
  .brand-blue { color: var(--blue); }
  .brand-stack { font-size: 8px; line-height: 9px; left: 17px; top: 232px; }

  .cover-title { position: absolute; color: var(--white); font-weight: 300; text-transform: uppercase; white-space: nowrap; }

  .slide-heading { position: absolute; left: 18px; top: 19px; font-size: 15px; font-weight: 400; color: var(--ink); }
  .slide-heading::after { content: ""; position: absolute; left: 0; top: 23px; width: 12px; height: 2px; background: var(--blue); box-shadow: 14px 0 0 -0.5px var(--blue); }
  .on-dark .slide-heading { color: var(--white); }
  .on-dark .slide-heading::after { background: var(--white); box-shadow: 14px 0 0 -0.5px var(--white); }

  .body-copy { position: absolute; left: 22px; width: 434px; font-size: 6.9px; line-height: 9px; color: var(--body); }
  .body-copy.first { top: 72px; } .body-copy.second { top: 148px; }
  .on-dark .body-copy { color: var(--white); }

  .footer-pill { position: absolute; left: 321px; top: 239px; width: 126px; height: 10px; border-radius: 5px; background: var(--blue); color: var(--white); font-size: 3.6px; line-height: 10px; text-align: center; white-space: nowrap; }
  .page-no { position: absolute; left: 455px; top: 239px; width: 10px; height: 10px; border-radius: 50%; background: var(--blue); color: var(--white); font-size: 5px; line-height: 10px; text-align: center; }

  .site-url { position: absolute; left: 20px; top: 237px; font-size: 6px; color: var(--white); }

  .agenda-label { position: absolute; left: 18px; top: 104px; font-size: 18px; font-weight: 400; color: var(--white); letter-spacing: 1px; text-transform: uppercase; }
  .agenda-label::after { content: ""; position: absolute; left: 1px; top: 26px; width: 12px; height: 2px; background: var(--white); box-shadow: 14px 0 0 -0.5px var(--white); }
  .agenda-item { position: absolute; display: flex; align-items: center; gap: 12px; font-size: 9px; color: var(--ink); }
  .agenda-item .num { width: 24px; height: 24px; border-radius: 50%; background: var(--blue); color: var(--white); font-size: 10px; line-height: 24px; text-align: center; }

  .break-title { position: absolute; left: 63px; top: 78px; font-size: 22px; line-height: 29px; color: var(--white); font-weight: 400; }
  .break-copy { position: absolute; left: 63px; top: 142px; width: 112px; font-size: 6.2px; line-height: 10px; color: var(--white); }
</style>
</head>
<body>
<div class="canvas">
<div class="deck">

  <!-- Cover A -->
  <section class="slide col-a row-1">
    <svg class="deco" viewBox="0 0 480 270" aria-hidden="true">
      <defs>
        <linearGradient id="cover-bg" x1="0" y1="0" x2="1" y2="1">
          <stop offset="0" stop-color="#3169d2"/><stop offset="1" stop-color="#1c4aa6"/>
        </linearGradient>
        <radialGradient id="soft-glow">
          <stop offset="0" stop-color="var(--glow)" stop-opacity="0.55"/>
          <stop offset="1" stop-color="var(--glow)" stop-opacity="0"/>
        </radialGradient>
        <radialGradient id="soft-shade">
          <stop offset="0" stop-color="var(--shade)" stop-opacity="0.7"/>
          <stop offset="1" stop-color="var(--shade)" stop-opacity="0"/>
        </radialGradient>
      </defs>
      <rect width="480" height="270" fill="url(#cover-bg)"/>
      <circle cx="470" cy="20" r="150" fill="url(#soft-glow)"/>
      <circle cx="40" cy="260" r="170" fill="url(#soft-shade)"/>
      <path d="M0 235 Q120 205 240 232 T480 222 V270 H0Z" fill="var(--shade)" opacity="0.45"/>
      <g stroke="var(--white)" stroke-width="1.5" fill="none">
        <path d="M90 160 V50 H380"/>
        <path d="M430 85 V200 H180"/>
      </g>
    </svg>
    <div class="brand brand-light" style="left:28px;top:94px;font-size:16px;">Norvale Works</div>
    <div class="cover-title" style="left:127px;top:132px;font-size:20px;">Your title goes here</div>
  </section>

  <!-- Cover B -->
  <section class="slide col-b row-1">
    <svg class="deco" viewBox="0 0 480 270" aria-hidden="true">
      <rect width="480" height="270" fill="url(#cover-bg)"/>
      <circle cx="60" cy="40" r="180" fill="url(#soft-shade)"/>
      <circle cx="400" cy="250" r="160" fill="url(#soft-glow)"/>
      <path d="M0 200 Q160 170 300 210 T480 190 V270 H0Z" fill="var(--shade)" opacity="0.35"/>
      <path d="M432 65 V125" stroke="var(--white)" stroke-width="1.5"/>
    </svg>
    <div class="brand brand-light" style="right:55px;top:70px;font-size:16px;">Norvale Works</div>
    <div class="cover-title" style="right:55px;top:97px;font-size:20px;">Your title goes here</div>
    <div class="site-url">www.norvaleworks.se</div>
  </section>

  <!-- Business title -->
  <section class="slide col-a row-2">
    <div class="photo" role="img" aria-label="Team collaborating around a table, washed in brand blue" style="inset:0;background:linear-gradient(120deg,#2c63cc 0%,#3a6fd2 45%,#2556b8 100%);"></div>
    <svg class="deco" viewBox="0 0 480 270" aria-hidden="true">
      <circle cx="420" cy="200" r="170" fill="url(#soft-shade)"/>
      <circle cx="300" cy="40" r="120" fill="url(#soft-glow)"/>
    </svg>
    <div class="brand brand-light" style="left:42px;top:37px;font-size:16px;">Norvale Works</div>
    <div class="cover-title" style="left:17px;top:110px;font-size:22px;line-height:27px;">This is your<br>business dev title</div>
  </section>

  <!-- Agenda -->
  <section class="slide col-b row-2">
    <svg class="deco" viewBox="0 0 480 270" aria-hidden="true">
      <defs>
        <linearGradient id="agenda-bg" x1="0" y1="0" x2="1" y2="1">
          <stop offset="0" stop-color="#1d4aa8"/><stop offset="1" stop-color="#3169d2"/>
        </linearGradient>
      </defs>
      <path d="M0 0 H123 L238 188 C252 212 240 232 215 245 L165 270 H0Z" fill="url(#agenda-bg)"/>
    </svg>
    <div class="agenda-label">Agenda</div>
    <div class="brand brand-light" style="left:20px;top:200px;font-size:21px;">Norvale Works</div>
    <div class="agenda-item" style="left:198px;top:16px;"><span class="num">01</span>Agenda 1</div>
    <div class="agenda-item" style="left:222px;top:52px;"><span class="num">02</span>Agenda 2</div>
    <div class="agenda-item" style="left:246px;top:88px;"><span class="num">03</span>Agenda 3</div>
    <div class="agenda-item" style="left:270px;top:124px;"><span class="num">04</span>Agenda 4</div>
    <div class="agenda-item" style="left:302px;top:160px;"><span class="num">05</span>Agenda 5</div>
    <div class="agenda-item" style="left:276px;top:203px;"><span class="num">06</span>Agenda 6</div>
  </section>

  <!-- Clean text -->
  <section class="slide col-a row-3">
    <h2 class="slide-heading">Clean and Bright Text Slides</h2>
    <p class="body-copy first">Technology only creates value when people know how to use it. We help leaders translate digital ambitions into clear priorities, practical roadmaps and everyday habits that last. Our teams work side by side with yours, mapping how decisions are made, where energy is lost and which tools truly move the business forward. We listen first, test ideas early and keep every step visible, so change feels shared rather than imposed. Workshops, pilots and coaching sessions turn insight into action across departments and borders. Every engagement ends with stronger relationships, shared ownership and measurable growth that keeps evolving long after we leave the room.</p>
    <p class="body-copy second">Technology only creates value when people know how to use it. We help leaders translate digital ambitions into clear priorities, practical roadmaps and everyday habits that last. Our teams work side by side with yours, mapping how decisions are made, where energy is lost and which tools truly move the business forward. We listen first, test ideas early and keep every step visible, so change feels shared rather than imposed. Workshops, pilots and coaching sessions turn insight into action across departments and borders. Every engagement ends with stronger relationships, shared ownership and measurable growth that keeps evolving long after we leave the room.</p>
    <div class="brand brand-blue brand-stack">Norvale<br>Works</div>
    <div class="footer-pill">© Copyright 2019 Norvale Works. All rights reserved.</div>
    <div class="page-no">5</div>
  </section>

  <!-- Bubble text light -->
  <section class="slide col-b row-3">
    <svg class="deco" viewBox="0 0 480 270" aria-hidden="true">
      <path d="M480 40 C440 55 430 110 400 150 C370 190 300 200 250 235 C225 252 215 262 212 270 H480Z" fill="var(--mist)"/>
      <path d="M480 120 C455 150 470 200 430 230 C410 245 380 250 360 270 H480Z" fill="#d3ddef"/>
    </svg>
    <h2 class="slide-heading">Normal (w bubbles) Text Slides</h2>
    <p class="body-copy first">Technology only creates value when people know how to use it. We help leaders translate digital ambitions into clear priorities, practical roadmaps and everyday habits that last. Our teams work side by side with yours, mapping how decisions are made, where energy is lost and which tools truly move the business forward. We listen first, test ideas early and keep every step visible, so change feels shared rather than imposed. Workshops, pilots and coaching sessions turn insight into action across departments and borders. Every engagement ends with stronger relationships, shared ownership and measurable growth that keeps evolving long after we leave the room.</p>
    <p class="body-copy second">Technology only creates value when people know how to use it. We help leaders translate digital ambitions into clear priorities, practical roadmaps and everyday habits that last. Our teams work side by side with yours, mapping how decisions are made, where energy is lost and which tools truly move the business forward. We listen first, test ideas early and keep every step visible, so change feels shared rather than imposed. Workshops, pilots and coaching sessions turn insight into action across departments and borders. Every engagement ends with stronger relationships, shared ownership and measurable growth that keeps evolving long after we leave the room.</p>
    <div class="brand brand-blue brand-stack">Norvale<br>Works</div>
    <div class="footer-pill">© Copyright 2019 Norvale Works. All rights reserved.</div>
    <div class="page-no">6</div>
  </section>

  <!-- Bubble text dark -->
  <section class="slide col-a row-4 on-dark" style="background:var(--navy);">
    <h2 class="slide-heading">Normal (w bubbles) Text Slides</h2>
    <p class="body-copy first">Technology only creates value when people know how to use it. We help leaders translate digital ambitions into clear priorities, practical roadmaps and everyday habits that last. Our teams work side by side with yours, mapping how decisions are made, where energy is lost and which tools truly move the business forward. We listen first, test ideas early and keep every step visible, so change feels shared rather than imposed. Workshops, pilots and coaching sessions turn insight into action across departments and borders. Every engagement ends with stronger relationships, shared ownership and measurable growth that keeps evolving long after we leave the room.</p>
    <p class="body-copy second">Technology only creates value when people know how to use it. We help leaders translate digital ambitions into clear priorities, practical roadmaps and everyday habits that last. Our teams work side by side with yours, mapping how decisions are made, where energy is lost and which tools truly move the business forward. We listen first, test ideas early and keep every step visible, so change feels shared rather than imposed. Workshops, pilots and coaching sessions turn insight into action across departments and borders. Every engagement ends with stronger relationships, shared ownership and measurable growth that keeps evolving long after we leave the room.</p>
    <div class="brand brand-light brand-stack">Norvale<br>Works</div>
    <div class="footer-pill">© Copyright 2019 Norvale Works. All rights reserved.</div>
    <div class="page-no">7</div>
  </section>

  <!-- Full photo -->
  <section class="slide col-b row-4">
    <div class="photo" role="img" aria-label="Consultant in a workshop leaning over a laptop" style="inset:0;background:linear-gradient(115deg,var(--photo-warm-a) 0%,#8a7563 45%,var(--photo-warm-b) 100%);"></div>
    <div class="brand brand-light brand-stack">Norvale<br>Works</div>
    <div class="footer-pill">© Copyright 2019 Norvale Works. All rights reserved.</div>
    <div class="page-no">8</div>
  </section>

  <!-- Two photos -->
  <section class="slide col-a row-5">
    <div class="photo" role="img" aria-label="Engineer working at an automated production line" style="left:0;top:25px;width:250px;height:110px;border-radius:0 55px 55px 0;background:linear-gradient(90deg,var(--photo-grey-a),var(--photo-grey-b));"></div>
    <div class="photo" role="img" aria-label="Two colleagues planning at a whiteboard" style="left:235px;top:118px;width:245px;height:110px;border-radius:55px 0 0 55px;background:linear-gradient(90deg,var(--photo-grey-b),#b9bcc2);"></div>
    <div class="brand brand-blue brand-stack">Norvale<br>Works</div>
    <div class="footer-pill">© Copyright 2019 Norvale Works. All rights reserved.</div>
    <div class="page-no">9</div>
  </section>

  <!-- Break section -->
  <section class="slide col-b row-5">
    <svg class="deco" viewBox="0 0 480 270" aria-hidden="true">
      <defs>
        <linearGradient id="break-bg" x1="0" y1="0" x2="1" y2="1">
          <stop offset="0" stop-color="#2a5fc8"/><stop offset="1" stop-color="#1c4aa6"/>
        </linearGradient>
      </defs>
      <path d="M0 0 H350 C420 40 455 110 448 180 C445 220 440 250 445 270 H0Z" fill="url(#break-bg)"/>
      <g stroke="var(--white)" stroke-width="1.2" fill="none">
        <path d="M49 68 V60 H57"/><path d="M183 60 H191 V68"/>
        <path d="M49 202 V210 H57"/><path d="M183 210 H191 V202"/>
      </g>
    </svg>
    <h2 class="break-title">Break<br>Section</h2>
    <p class="break-copy">A wonderful serenity has taken possession of my entire soul, like these sweet mornings of spring which I enjoy with my whole heart. I am alone, and feel the charm</p>
  </section>

</div>
</div>
</body>
</html>
```